body balm label design

body balm tube design, current label design for other similar products
Need to have a design which can interchange between 3 different solutions
Amber Tide (Lavender + Vanilla)
Copper Harbor (Eucalyptus + Mint)
Velvet Arc (Bergamot + Cedarwood)
Tube size:
2.5h x 3.25 w
Target Market(s)
natural, solution focused
Requirements
Must have
- relatable to existing brand designs, focus on features and benefits

```html
<!DOCTYPE html>
<html lang="en">
<head>
<meta charset="utf-8">
<title>Terra Leaf Natural Body Spray Labels</title>
<link rel="stylesheet" href="https://fonts.googleapis.com/css2?family=Playfair+Display:wght@400;500&family=Barlow:wght@400&family=Allura&family=Sacramento&display=swap">
<style>
  :root {
    --backdrop: #c9cbca;
    --paper: #ffffff;
    --ink: #2a2526;
    --arch: #5e5c5d;
    --arch-text: #f2f2f2;
    --lavender: #a57ca6;
    --vanilla: #e6d13e;
    --eucalyptus: #2d7a57;
    --mint: #5bb54a;
    --bergamot: #6ea36f;
    --cedar: #9b7635;
    --botanical-light: #f0f0f0;
    --botanical-mid: #a6a6a6;
    --botanical-dark: #5a5a5a;
  }
  * { margin: 0; padding: 0; box-sizing: border-box; }
  html, body { width: 1200px; height: 946px; overflow: hidden; background: var(--backdrop); }
  .canvas { position: relative; width: 1200px; height: 946px; }

  .label {
    position: absolute;
    width: 772px; height: 562px;
    background: var(--paper);
    transform-origin: 0 0;
    transform: scale(0.5538);
    color: var(--ink);
    font-family: "Playfair Display", serif;
    overflow: hidden;
  }
  .label--amber { left: 176px; top: 183px; }
  .label--copper { left: 672px; top: 183px; }
  .label--velvet { left: 424px; top: 553px; }

  .vertical {
    position: absolute;
    writing-mode: vertical-rl;
    transform: rotate(180deg);
  }

  .rule { position: absolute; left: 65px; width: 3px; height: 47px; background: var(--ink); }
  .rule--top { top: 0; }
  .rule--bottom { bottom: 0; }

  .product-name {
    left: 20px; top: 47px; width: 90px; height: 468px;
    display: flex; align-items: center; justify-content: center;
    font-size: 62px; font-weight: 400; line-height: 1; white-space: nowrap;
    text-transform: uppercase;
  }
  .label--copper .product-name { font-size: 54px; }

  .arch {
    position: absolute; left: 146px; top: 0; width: 133px; height: 291px;
    background: var(--arch);
    border-radius: 0 0 66.5px 66.5px;
    color: var(--arch-text);
    text-align: center;
  }
  .arch__brand { position: absolute; top: 26px; width: 100%; font-size: 10px; letter-spacing: 1.5px; }
  .arch__type {
    position: absolute; top: 120px; width: 100%;
    font-family: "Barlow", sans-serif; font-size: 16px; line-height: 19px;
  }
  .arch__type span { display: block; letter-spacing: 3.5px; }
  .arch__type span + span { letter-spacing: 1px; }
  .arch__curve { position: absolute; left: 0; top: 0; width: 133px; height: 291px; }
  .arch__curve text { font-family: "Playfair Display", serif; font-size: 8.5px; fill: var(--arch-text); letter-spacing: 0.8px; }

  .scent { position: absolute; left: 112px; top: 366px; width: 200px; text-align: center; }
  .scent__base { font-size: 21px; letter-spacing: 1.5px; line-height: 1; }
  .scent__accent { font-family: "Sacramento", cursive; font-size: 60px; line-height: 1; margin-top: 4px; }
  .label--amber .scent__base { color: var(--lavender); }
  .label--amber .scent__accent { color: var(--vanilla); }
  .label--copper .scent__base { color: var(--eucalyptus); }
  .label--copper .scent__accent { color: var(--mint); }
  .label--velvet .scent__base { color: var(--bergamot); }
  .label--velvet .scent__accent { color: var(--cedar); }

  .origin-badge {
    position: absolute; left: 279px; top: 481px; width: 36px; height: 36px;
    border: 1px solid var(--ink); border-radius: 50%;
  }
  .net-weight { position: absolute; left: 112px; top: 532px; width: 200px; text-align: center; font-size: 9px; }
  .label--amber .net-weight { color: var(--lavender); }

  .botanical {
    position: absolute; left: 337px; top: 12px; width: 210px; height: 550px;
    background: linear-gradient(175deg, var(--botanical-light) 0%, var(--botanical-mid) 35%, var(--botanical-light) 55%, var(--botanical-mid) 80%, var(--botanical-dark) 100%);
    opacity: 0.55;
    border-radius: 40px 40px 0 0;
  }

  .claims {
    left: 570px; top: 31px; height: 500px; width: 36px;
    display: flex; justify-content: space-between; align-items: center;
    font-family: "Allura", cursive; font-size: 32px; line-height: 1;
  }
  .claims__line { position: absolute; left: 612px; top: 31px; width: 1.5px; height: 500px; background: var(--ink); }

  .ingredients {
    left: 620px; top: 30px; height: 510px; width: 100px;
    text-align: center; font-size: 10.5px; line-height: 13px;
  }
  .ingredients h2 { font-size: 14px; font-weight: 500; line-height: 20px; }

  .maker { left: 738px; top: 175px; height: 180px; width: 14px; font-size: 7px; line-height: 14px; text-align: center; }
  .website { left: 738px; top: 400px; height: 90px; width: 14px; font-size: 7px; line-height: 14px; text-align: center; }
</style>
</head>
<body>
<main class="canvas">

  <section class="label label--amber">
    <span class="rule rule--top"></span>
    <h1 class="vertical product-name">Amber Tide</h1>
    <span class="rule rule--bottom"></span>
    <div class="arch">
      <p class="arch__brand">TERRA LEAF</p>
      <p class="arch__type"><span>NATURAL</span><span>BODY SPRAY</span></p>
      <svg class="arch__curve" viewBox="0 0 133 291" aria-hidden="true">
        <defs><path id="curve-amber" d="M 14.5 224.5 A 52 52 0 0 0 118.5 224.5"/></defs>
        <text><textPath href="#curve-amber" startOffset="50%" text-anchor="middle">PLANT · BASED · AROMATHERAPY</textPath></text>
      </svg>
    </div>
    <div class="scent"><p class="scent__base">LAVENDER +</p><p class="scent__accent">Vanilla</p></div>
    <span class="origin-badge"></span>
    <p class="net-weight">Net WT. 3oz</p>
    <div class="botanical" role="img" aria-label="Greyscale botanical illustration of lavender sprigs, lilies, citrus halves, pine cones and eucalyptus leaves"></div>
    <p class="vertical claims"><span>Plant Based</span><span>·</span><span>Vegan</span><span>·</span><span>Cruelty Free</span></p>
    <span class="claims__line"></span>
    <div class="vertical ingredients">
      <h2>Ingredients</h2>
      <p>Lorem Ipsum is simply dummy text of the printing and typesetting industry. Lorem Ipsum has been the industry's standard dummy text ever since the 1500s, when an unknown printer took a galley of type and scrambled it to make a type specimen book. It has survived not only five centuries, but also the leap into electronic typesetting, remaining essentially unchanged.</p>
    </div>
    <p class="vertical maker">Made by Terra Leaf, Fernvale, AB T0L 2B3</p>
    <p class="vertical website">www.terraleaf.ca</p>
  </section>

  <section class="label label--copper">
    <span class="rule rule--top"></span>
    <h1 class="vertical product-name">Copper Harbor</h1>
    <span class="rule rule--bottom"></span>
    <div class="arch">
      <p class="arch__brand">TERRA LEAF</p>
      <p class="arch__type"><span>NATURAL</span><span>BODY SPRAY</span></p>
      <svg class="arch__curve" viewBox="0 0 133 291" aria-hidden="true">
        <defs><path id="curve-copper" d="M 14.5 224.5 A 52 52 0 0 0 118.5 224.5"/></defs>
        <text><textPath href="#curve-copper" startOffset="50%" text-anchor="middle">PLANT · BASED · AROMATHERAPY</textPath></text>
      </svg>
    </div>
    <div class="scent"><p class="scent__base">EUCALYPTUS +</p><p class="scent__accent">Mint</p></div>
    <span class="origin-badge"></span>
    <p class="net-weight">Net WT. 3oz</p>
    <div class="botanical" role="img" aria-label="Greyscale botanical illustration of lavender sprigs, lilies, citrus halves, pine cones and eucalyptus leaves"></div>
    <p class="vertical claims"><span>Plant Based</span><span>·</span><span>Vegan</span><span>·</span><span>Cruelty Free</span></p>
    <span class="claims__line"></span>
    <div class="vertical ingredients">
      <h2>Ingredients</h2>
      <p>Lorem Ipsum is simply dummy text of the printing and typesetting industry. Lorem Ipsum has been the industry's standard dummy text ever since the 1500s, when an unknown printer took a galley of type and scrambled it to make a type specimen book. It has survived not only five centuries, but also the leap into electronic typesetting, remaining essentially unchanged.</p>
    </div>
    <p class="vertical maker">Made by Terra Leaf, Fernvale, AB T0L 2B3</p>
    <p class="vertical website">www.terraleaf.ca</p>
  </section>

  <section class="label label--velvet">
    <span class="rule rule--top"></span>
    <h1 class="vertical product-name">Velvet Arc</h1>
    <span class="rule rule--bottom"></span>
    <div class="arch">
      <p class="arch__brand">TERRA LEAF</p>
      <p class="arch__type"><span>NATURAL</span><span>BODY SPRAY</span></p>
      <svg class="arch__curve" viewBox="0 0 133 291" aria-hidden="true">
        <defs><path id="curve-velvet" d="M 14.5 224.5 A 52 52 0 0 0 118.5 224.5"/></defs>
        <text><textPath href="#curve-velvet" startOffset="50%" text-anchor="middle">PLANT · BASED · AROMATHERAPY</textPath></text>
      </svg>
    </div>
    <div class="scent"><p class="scent__base">BERGAMOT +</p><p class="scent__accent">Cedarwood</p></div>
    <span class="origin-badge"></span>
    <p class="net-weight">Net WT. 3oz</p>
    <div class="botanical" role="img" aria-label="Greyscale botanical illustration of lavender sprigs, lilies, citrus halves, pine cones and eucalyptus leaves"></div>
    <p class="vertical claims"><span>Plant Based</span><span>·</span><span>Vegan</span><span>·</span><span>Cruelty Free</span></p>
    <span class="claims__line"></span>
    <div class="vertical ingredients">
      <h2>Ingredients</h2>
      <p>Lorem Ipsum is simply dummy text of the printing and typesetting industry. Lorem Ipsum has been the industry's standard dummy text ever since the 1500s, when an unknown printer took a galley of type and scrambled it to make a type specimen book. It has survived not only five centuries, but also the leap into electronic typesetting, remaining essentially unchanged.</p>
    </div>
    <p class="vertical maker">Made by Terra Leaf, Fernvale, AB T0L 2B3</p>
    <p class="vertical website">www.terraleaf.ca</p>
  </section>

</main>
</body>
</html>
```